Treatment Info-Graphic Poster

22 x 28 poster. We need a design for a poster to hang in our treatment rooms that quickly compares different treatments we offer and sets expectations for the patient. Attached is something I very quickly created on Excel, but we would like one that matches our company colors and looks much more polished. I have attached a info-graphic we have had designed prior for reference.

Target Market(s)

Osteoarthritis of the knee patients treatment comparison info graphic for poster

Font styles to use
Serif

Colors
85cae6
f78f20

Requirements
Must have
• Branded treatment comparison table
Nice to have
• Treatment graphics

```html
<!DOCTYPE html>
<html lang="en">
<head>
<meta charset="utf-8">
<title>Knee Treatment Comparison Poster</title>
<link href="https://fonts.googleapis.com/css2?family=Montserrat:wght@700&family=Questrial&display=swap" rel="stylesheet">
<style>
  :root {
    --page: #ffffff;
    --panel-light: #8a8a8a;
    --panel-dark: #3c3c3c;
    --brand-teal: #3fb0cc;
    --brand-sky: #85cae6;
    --label-blue: #1565c0;
    --white: #ffffff;
    --tagline: #5f5f5f;
  }
  html, body { margin: 0; padding: 0; width: 1200px; height: 1200px; overflow: hidden; background: var(--page); }
  .poster { position: relative; width: 1200px; height: 1200px; }
  .panel {
    position: absolute; left: 0; top: 128px; width: 1200px; height: 944px;
    background: radial-gradient(ellipse 60% 60% at 55% 50%, var(--panel-light), var(--panel-dark));
  }
  .brand { position: absolute; left: 14px; top: 138px; }
  .brand-bar {
    display: flex; align-items: center; gap: 14px;
    width: 196px; height: 92px; padding-left: 18px;
    background: linear-gradient(180deg, #5cc3dc, var(--brand-teal));
    border-radius: 8px; box-shadow: 0 3px 8px rgba(0,0,0,.35);
  }
  .brand-mark { width: 18px; height: 18px; background: var(--white); }
  .brand-name { font-family: "Questrial", sans-serif; font-size: 38px; color: var(--white); }
  .tagline { margin: 10px 0 0 20px; font-family: "Questrial", sans-serif; font-size: 19px; color: var(--tagline); }

  .label {
    position: absolute; font-family: "Montserrat", sans-serif; font-weight: 700;
    font-size: 9.5px; line-height: 1.4; letter-spacing: 0.2px;
    color: var(--label-blue); text-align: center; text-transform: uppercase;
    text-shadow: 1px 0 0 var(--white), -1px 0 0 var(--white), 0 1px 0 var(--white), 0 -1px 0 var(--white),
                 1px 1px 0 var(--white), -1px -1px 0 var(--white), 1px -1px 0 var(--white), -1px 1px 0 var(--white);
    transform: translate(-50%, -50%);
    white-space: nowrap;
  }
  .label.small { font-size: 8px; }
  .label.large { font-size: 11px; }

  .badge { position: absolute; transform: translate(-50%, -50%); }
  .badge.head { width: 64px; height: 64px; }
  .badge.row { width: 40px; height: 40px; }

  .tick { position: absolute; width: 36px; height: 30px; transform: translate(-50%, -50%); }
</style>
</head>
<body>
<div class="poster">
  <div class="panel"></div>

  <div class="brand">
    <div class="brand-bar"><span class="brand-mark"></span><span class="brand-name">Kinetra</span></div>
    <div class="tagline">Move freely again.</div>
  </div>

  <svg width="0" height="0" style="position:absolute">
    <defs>
      <radialGradient id="orb" cx="40%" cy="35%" r="70%">
        <stop offset="0" stop-color="#4aa3ee"/>
        <stop offset="1" stop-color="#0e4f9a"/>
      </radialGradient>
      <symbol id="disc" viewBox="0 0 64 64">
        <circle cx="32" cy="34" r="30" fill="#000" opacity=".3"/>
        <circle cx="32" cy="32" r="30" fill="#dfe9f5"/>
        <circle cx="32" cy="32" r="26" fill="url(#orb)"/>
      </symbol>
      <symbol id="check" viewBox="0 0 36 30">
        <path d="M3 15 L13 25 L33 4" fill="none" stroke="#fff" stroke-width="8" stroke-linecap="round" stroke-linejoin="round"/>
        <path d="M3 15 L13 25 L33 4" fill="none" stroke="#2f78d6" stroke-width="4" stroke-linecap="round" stroke-linejoin="round"/>
      </symbol>
    </defs>
  </svg>

  <!-- column headers -->
  <div class="label" style="left:394px;top:326px">Hyaluronic Acid<br>(HA)</div>
  <svg class="badge head" style="left:490px;top:322px" viewBox="0 0 64 64"><use href="#disc"/><path d="M28 16h8v6h3v26h-14v-26h3z" fill="#fff"/></svg>

  <div class="label small" style="left:592px;top:319px">Platelet Rich<br>Plasma (PRP)</div>
  <svg class="badge head" style="left:678px;top:322px" viewBox="0 0 64 64"><use href="#disc"/><path d="M22 44 L42 20 M40 18 L46 24 M24 42 L18 48" stroke="#fff" stroke-width="3" stroke-linecap="round"/></svg>

  <div class="label small" style="left:784px;top:319px">Stem Cell<br>Theraphy + PRP</div>
  <svg class="badge head" style="left:872px;top:322px" viewBox="0 0 64 64"><use href="#disc"/><path d="M14 24 C26 24 38 40 50 40 M14 40 C26 40 38 24 50 24" fill="none" stroke="#fff" stroke-width="2.5"/></svg>

  <div class="label large" style="left:972px;top:320px">Knee Brace(s)</div>
  <svg class="badge head" style="left:1064px;top:322px" viewBox="0 0 64 64" role="img" aria-label="Runner graphic"><use href="#disc"/></svg>

  <!-- row labels and icons -->
  <div class="label" style="left:212px;top:374px">Cusion &amp; Lubricate</div>
  <svg class="badge row" style="left:318px;top:374px" viewBox="0 0 64 64"><use href="#disc"/><rect x="20" y="20" width="24" height="24" rx="3" fill="#fff"/></svg>

  <div class="label" style="left:211px;top:429px">Decrease Inflammation</div>
  <svg class="badge row" style="left:318px;top:430px" viewBox="0 0 64 64"><use href="#disc"/><g fill="none" stroke="#fff" stroke-width="2"><circle cx="32" cy="32" r="16"/><circle cx="32" cy="32" r="10"/><circle cx="32" cy="32" r="4"/></g></svg>

  <div class="label" style="left:216px;top:486px">Stimulates Synovial<br>Production of HA</div>
  <svg class="badge row" style="left:318px;top:486px" viewBox="0 0 64 64" role="img" aria-label="Knee joint graphic"><use href="#disc"/></svg>

  <div class="label large" style="left:216px;top:541px">Healing Properties</div>
  <svg class="badge row" style="left:318px;top:542px" viewBox="0 0 64 64"><use href="#disc"/><path d="M32 18v28M18 32h28" stroke="#fff" stroke-width="8" stroke-linecap="round"/></svg>

  <div class="label" style="left:216px;top:598px">Repairative Properties</div>
  <svg class="badge row" style="left:318px;top:598px" viewBox="0 0 64 64"><use href="#disc"/><path d="M26 22v16M18 30h16M40 28v12M34 34h12M32 40v8M28 44h8" stroke="#fff" stroke-width="4" stroke-linecap="round"/></svg>

  <div class="label small" style="left:220px;top:652px">Potential Cartilage<br>Regeneration</div>
  <svg class="badge row" style="left:318px;top:654px" viewBox="0 0 64 64" role="img" aria-label="Cartilage joint graphic"><use href="#disc"/></svg>

  <div class="label" style="left:218px;top:710px">On Average, Benefits<br>Last 4-6 Months</div>
  <svg class="badge row" style="left:318px;top:710px" viewBox="0 0 64 64"><use href="#disc"/><rect x="20" y="20" width="24" height="24" rx="2" fill="none" stroke="#fff" stroke-width="2.5"/><path d="M25 32l5 5 9-10" fill="none" stroke="#fff" stroke-width="2.5"/></svg>

  <div class="label" style="left:218px;top:766px">On Average, Benefits<br>Last 6-12 Months</div>
  <svg class="badge row" style="left:318px;top:766px" viewBox="0 0 64 64"><use href="#disc"/><rect x="20" y="20" width="24" height="24" rx="2" fill="none" stroke="#fff" stroke-width="2.5"/><path d="M25 32l5 5 9-10" fill="none" stroke="#fff" stroke-width="2.5"/></svg>

  <div class="label" style="left:218px;top:822px">On Average, Benefits<br>Last 18+ Months</div>
  <svg class="badge row" style="left:318px;top:822px" viewBox="0 0 64 64"><use href="#disc"/><rect x="20" y="20" width="24" height="24" rx="2" fill="none" stroke="#fff" stroke-width="2.5"/><path d="M25 32l5 5 9-10" fill="none" stroke="#fff" stroke-width="2.5"/></svg>

  <div class="label small" style="left:218px;top:876px">Corrects Biomechanics<br>&amp; Stabilizes Joint</div>
  <svg class="badge row" style="left:318px;top:878px" viewBox="0 0 64 64" role="img" aria-label="Foot and ankle graphic"><use href="#disc"/></svg>

  <div class="label small" style="left:218px;top:932px">Covered by Most<br>Insurance</div>
  <svg class="badge row" style="left:318px;top:933px" viewBox="0 0 64 64"><use href="#disc"/><path d="M32 16l14 5v10c0 9-6 15-14 18-8-3-14-9-14-18V21z" fill="none" stroke="#fff" stroke-width="2.5"/><path d="M25 32l5 5 9-10" fill="none" stroke="#fff" stroke-width="2.5"/></svg>

  <!-- ticks: hyaluronic acid -->
  <svg class="tick" style="left:490px;top:375px"><use href="#check"/></svg>
  <svg class="tick" style="left:490px;top:430px"><use href="#check"/></svg>
  <svg class="tick" style="left:490px;top:486px"><use href="#check"/></svg>
  <svg class="tick" style="left:490px;top:710px"><use href="#check"/></svg>
  <svg class="tick" style="left:490px;top:933px"><use href="#check"/></svg>

  <!-- ticks: platelet rich plasma -->
  <svg class="tick" style="left:678px;top:375px"><use href="#check"/></svg>
  <svg class="tick" style="left:678px;top:430px"><use href="#check"/></svg>
  <svg class="tick" style="left:678px;top:486px"><use href="#check"/></svg>
  <svg class="tick" style="left:678px;top:542px"><use href="#check"/></svg>
  <svg class="tick" style="left:678px;top:710px"><use href="#check"/></svg>
  <svg class="tick" style="left:678px;top:766px"><use href="#check"/></svg>

  <!-- ticks: stem cell therapy -->
  <svg class="tick" style="left:872px;top:375px"><use href="#check"/></svg>
  <svg class="tick" style="left:872px;top:430px"><use href="#check"/></svg>
  <svg class="tick" style="left:872px;top:486px"><use href="#check"/></svg>
  <svg class="tick" style="left:872px;top:542px"><use href="#check"/></svg>
  <svg class="tick" style="left:872px;top:598px"><use href="#check"/></svg>
  <svg class="tick" style="left:872px;top:654px"><use href="#check"/></svg>
  <svg class="tick" style="left:872px;top:710px"><use href="#check"/></svg>
  <svg class="tick" style="left:872px;top:766px"><use href="#check"/></svg>
  <svg class="tick" style="left:872px;top:822px"><use href="#check"/></svg>

  <!-- ticks: knee brace -->
  <svg class="tick" style="left:1064px;top:710px"><use href="#check"/></svg>
  <svg class="tick" style="left:1064px;top:766px"><use href="#check"/></svg>
  <svg class="tick" style="left:1064px;top:822px"><use href="#check"/></svg>
  <svg class="tick" style="left:1064px;top:878px"><use href="#check"/></svg>
  <svg class="tick" style="left:1064px;top:933px"><use href="#check"/></svg>
</div>
</body>
</html>
```